Dentistry

Dentist's personal business card. No logo needed. The card shoul deliver the massage of reliability, professionalism, experience.
Please ad the full brief of the project: down the line it says: the winning look should be precise and pristine NO pictures of Teeth, smiles, instruments etc.

The details to be desplaid are:
Dr. Rob Valdoni
Doctor of Dental Surgery
PHD
Web. Www.drvaldoni.com
Email. Rob@drvaldoni.com
Tel 07731482590
Surgery address. 27Bharwick road London SW4 7QN UK
82 Fenwyn Row London SW3 2HT. Uk

Reason: Decided to make the payment unrefundable in order to get more designers involved.

Requirements
Should not have
• Logo, teeth, smile any sort of instruments.

```html
<!DOCTYPE html>
<html lang="en">
<head>
<meta charset="utf-8">
<title>Dr. Rob Valdoni — Business Card</title>
<link rel="stylesheet" href="https://fonts.googleapis.com/css2?family=Arimo:wght@400;700&display=swap">
<style>
  :root {
    --stage: #2b2e30;
    --card-white: #f4f4f2;
    --card-white-tone: #e9e9e6;
    --card-teal: #1d5a6d;
    --card-teal-tone: #236578;
    --ink-dark: #1b1b1b;
    --ink-light: #e8eef0;
  }
  * { box-sizing: border-box; margin: 0; padding: 0; }
  html, body {
    width: 1200px;
    height: 800px;
    overflow: hidden;
    background: var(--stage);
    font-family: "Arimo", Arial, sans-serif;
  }
  .stage {
    width: 1200px;
    height: 800px;
    display: flex;
    align-items: center;
    justify-content: center;
    gap: 60px;
  }
  .card {
    position: relative;
    width: 520px;
    height: 297px;
    border-radius: 2px;
    overflow: hidden;
    box-shadow: 0 10px 30px rgba(0, 0, 0, 0.35);
  }
  .card-texture {
    position: absolute;
    inset: 0;
  }
  .card--front { color: var(--ink-dark); }
  .card--front .card-texture {
    background: linear-gradient(135deg, var(--card-white) 0%, var(--card-white-tone) 100%);
  }
  .card--back { color: var(--ink-light); }
  .card--back .card-texture {
    background: linear-gradient(135deg, var(--card-teal-tone) 0%, var(--card-teal) 100%);
  }
  .identity {
    position: absolute;
    left: 300px;
    top: 112px;
  }
  .identity-name {
    font-weight: 700;
    font-size: 20px;
    letter-spacing: 0.2px;
    text-transform: uppercase;
    line-height: 1.1;
    white-space: nowrap;
  }
  .identity-role {
    font-size: 11px;
    line-height: 1.35;
    margin-top: 3px;
  }
  .contact {
    position: absolute;
    left: 62px;
    top: 174px;
    font-size: 12px;
    line-height: 1.42;
    white-space: nowrap;
  }
  .contact-label { font-weight: 700; }
  .contact-addresses { margin-top: 9px; }
</style>
</head>
<body>
<main class="stage">
  <article class="card card--front">
    <div class="card-texture" role="img" aria-label="Faint embossed damask pattern on white card stock"></div>
    <div class="identity">
      <p class="identity-name">Dr. Rob Valdoni</p>
      <p class="identity-role">Doctor of Dental Surgery<br>PhD</p>
    </div>
    <div class="contact">
      <p><span class="contact-label">Tel:</span> 07731482590</p>
      <p><span class="contact-label">Email:</span> Rob@drvaldoni.com</p>
      <p><span class="contact-label">Web:</span> Www.drvaldoni.com</p>
      <div class="contact-addresses">
        <p>27Bharwick road London SW4 7QN UK</p>
        <p>82 Fenwyn Row London SW3 2HT. Uk</p>
      </div>
    </div>
  </article>

  <article class="card card--back">
    <div class="card-texture" role="img" aria-label="Faint damask pattern on deep teal card stock"></div>
    <div class="identity">
      <p class="identity-name">Dr. Rob Valdoni</p>
      <p class="identity-role">Doctor of Dental Surgery<br>PhD</p>
    </div>
    <div class="contact">
      <p><span class="contact-label">Tel:</span> 07731482590</p>
      <p><span class="contact-label">Email:</span> Rob@drvaldoni.com</p>
      <p><span class="contact-label">Web:</span> Www.drvaldoni.com</p>
      <div class="contact-addresses">
        <p>27Bharwick road London SW4 7QN UK</p>
        <p>82 Fenwyn Row London SW3 2HT. Uk</p>
      </div>
    </div>
  </article>
</main>
</body>
</html>
```